Folder and Swag Design for Law Firm

We are a personal injury law firm designing new client materials for folders and other swag that will go to clients once they retain us. Rather than just being white on green, or green on white, we'd like a design to put on the items. One idea that we had was a wave that included our slogan of "Our family protecting yours" that can wrap around a folder, or a tumbler but we are open to other ideas. I've attached a sketch of the wave design and our logo.
The final design should communicate a family protective feel.
Branding colors: #FFFFFF, #0FA57B, #00CA88
Victims of personal injury (car accidents, slip and falls, defective products).
Legal Services

```html
<!DOCTYPE html>
<html lang="en">
<head>
<meta charset="utf-8">
<title>Harlow &amp; Benton Folder</title>
<link href="https://fonts.googleapis.com/css2?family=Fira+Sans:wght@700&family=Open+Sans:wght@400;600;700&family=Sacramento&display=swap" rel="stylesheet">
<style>
  :root{
    --white:#FFFFFF;
    --green:#0FA57B;
    --mint:#00CA88;
    --navy:#1E323B;
    --stage:#A8A8A8;
    --ink:#2b3a40;
  }
  *{margin:0;padding:0;box-sizing:border-box}
  html,body{width:1200px;height:1200px;overflow:hidden;background:var(--stage)}
  .canvas{position:relative;width:1200px;height:1200px}
  .folder-art{position:absolute;left:0;top:0}
  .brand{position:absolute;left:688px;top:299px;display:flex;align-items:center;gap:10px}
  .brand-square{width:53px;height:44px;background:#3AA77D}
  .brand-name{font-family:"Open Sans",sans-serif;font-weight:600;font-size:14px;letter-spacing:1.5px;color:#3AA77D;text-transform:uppercase}
  .slogan{position:absolute;left:268px;top:470px;width:520px;font-family:"Sacramento",cursive;font-size:62px;color:var(--white);white-space:nowrap;transform:rotate(-16.4deg);transform-origin:left center}
  .address-pill{position:absolute;left:324px;top:723px;width:227px;height:21px;border:1px solid var(--white);border-radius:11px;display:flex;align-items:center;justify-content:center;font-family:"Open Sans",sans-serif;font-weight:700;font-size:8.6px;color:var(--white)}
  .reviews-title{position:absolute;left:689px;top:638px;font-family:"Fira Sans",sans-serif;font-weight:700;font-size:15.5px;color:var(--mint)}
  .highlights{position:absolute;left:689px;top:665px;width:240px;display:grid;grid-template-columns:131px 109px;row-gap:11px;list-style:none}
  .highlights li{display:flex;gap:6px;font-family:"Open Sans",sans-serif;font-size:6px;line-height:8px;color:var(--ink)}
  .tick{flex:none;width:6px;height:6px;border-radius:50%;background:var(--mint);position:relative;top:1px}
  .tick::after{content:"";position:absolute;left:1.7px;top:1px;width:1.6px;height:2.6px;border:solid var(--white);border-width:0 0.8px 0.8px 0;transform:rotate(45deg)}
  .contact-bar{position:absolute;left:686px;top:725px;height:20px;display:flex;font-family:"Open Sans",sans-serif;color:var(--white)}
  .contact-phone{background:var(--navy);border-radius:10px 0 0 10px;padding:0 14px 0 6px;display:flex;align-items:center;gap:4px;font-size:9.5px;font-weight:600}
  .contact-web{background:var(--mint);border-radius:10px;margin-left:-6px;padding:0 8px 0 7px;display:flex;align-items:center;gap:5px;font-size:7.5px;font-weight:600}
  .icon-dot{width:11px;height:11px;border-radius:50%;background:var(--mint);display:flex;align-items:center;justify-content:center}
  .contact-web .icon-dot{background:var(--navy)}
</style>
</head>
<body>
<div class="canvas">
  <svg class="folder-art" width="1200" height="1200" viewBox="0 0 1200 1200">
    <defs>
      <linearGradient id="familyTones" x1="0" y1="0" x2="1" y2="1">
        <stop offset="0" stop-color="#7a8a2e"/>
        <stop offset="0.45" stop-color="#d8b45a"/>
        <stop offset="0.8" stop-color="#b98a4a"/>
        <stop offset="1" stop-color="#5d6e2a"/>
      </linearGradient>
      <linearGradient id="bandTone" x1="0" y1="0" x2="1" y2="0">
        <stop offset="0.55" stop-color="#1E323B"/>
        <stop offset="1" stop-color="#3b4448"/>
      </linearGradient>
      <linearGradient id="teamTones" x1="0" y1="0" x2="1" y2="0">
        <stop offset="0" stop-color="#5a6064" stop-opacity="0"/>
        <stop offset="0.35" stop-color="#5a6064" stop-opacity="0.75"/>
        <stop offset="1" stop-color="#6a6e70"/>
      </linearGradient>
      <linearGradient id="whiteFold" x1="0" y1="0" x2="1" y2="0">
        <stop offset="0" stop-color="#e2e4e4"/>
        <stop offset="0.2" stop-color="#ffffff"/>
      </linearGradient>
      <linearGradient id="pocketTone" x1="0" y1="0" x2="0" y2="1">
        <stop offset="0" stop-color="#0FA57B"/>
        <stop offset="0.6" stop-color="#00CA88"/>
      </linearGradient>
    </defs>

    <!-- side flap -->
    <polygon class="side-flap" points="217,600 250,590 250,762 217,753" fill="var(--mint)"/>

    <!-- pocket -->
    <polygon class="pocket" points="250,762 614,762 606,935 250,935" fill="url(#pocketTone)"/>
    <g class="card-slits" stroke="var(--white)" stroke-width="0.8">
      <line x1="317" y1="828" x2="343" y2="812"/>
      <line x1="491" y1="812" x2="519" y2="828"/>
      <line x1="317" y1="860" x2="343" y2="876"/>
      <line x1="491" y1="876" x2="519" y2="860"/>
    </g>

    <!-- front panel top photo and back panel top -->
    <rect class="family-photo" role="img" aria-label="Photo of a happy family playing outdoors at sunset" x="250" y="266" width="367" height="300" fill="url(#familyTones)"/>
    <rect class="brand-header" x="617" y="266" width="367" height="200" fill="var(--navy)"/>

    <!-- wave layers -->
    <path class="wave-outer" fill="var(--green)" d="M250,512 C330,470 400,440 470,445 C540,450 570,428 617,428 C660,428 680,405 700,385 C730,355 765,352 800,370 C840,392 870,398 910,378 C940,362 960,338 984,334 L984,762 L250,762Z"/>
    <path class="wave-band" fill="url(#bandTone)" d="M250,535 C330,495 400,470 470,470 C540,470 580,447 617,446 C665,445 690,420 712,398 C740,372 770,374 805,392 C840,410 875,414 910,396 C940,380 962,360 984,357 L984,762 L250,762Z"/>
    <path class="team-photo" role="img" aria-label="Portrait photo of the three firm attorneys" fill="url(#teamTones)" d="M640,434 C670,432 690,420 712,398 C740,372 770,374 805,392 C840,410 875,414 910,396 C940,380 962,360 984,357 L984,540 C950,540 920,565 890,585 C860,605 830,610 790,595 C760,585 730,575 700,605 C680,625 660,634 640,634Z"/>
    <path class="wave-lower" fill="var(--green)" d="M250,713 C310,680 360,660 400,665 C440,670 470,665 500,645 C540,620 570,630 617,632 C660,634 680,620 700,600 C730,570 760,580 790,590 C830,605 860,600 890,580 C920,560 950,535 984,536 L984,762 L250,762Z"/>
    <path class="front-base" fill="var(--mint)" d="M250,732 C300,702 350,674 395,678 C430,682 460,690 500,668 C540,646 575,650 617,652 L617,762 L250,762Z"/>
    <path class="back-base" fill="url(#whiteFold)" d="M617,652 C660,654 680,640 700,620 C730,590 760,598 790,608 C830,622 860,618 890,598 C920,578 950,555 984,556 L984,762 L617,762Z"/>

    <!-- pin above address -->
    <circle class="pin-badge" cx="438" cy="720" r="8" fill="var(--mint)" stroke="var(--white)" stroke-width="1"/>
    <path class="pin-icon" fill="var(--white)" d="M438,715 a3,3 0 0 1 3,3 c0,2 -3,5 -3,5 c0,0 -3,-3 -3,-5 a3,3 0 0 1 3,-3Z"/>
  </svg>

  <div class="brand">
    <span class="brand-square"></span>
    <span class="brand-name">Harlow &amp; Benton, LLC</span>
  </div>

  <div class="slogan">Our family protecting yours</div>

  <div class="address-pill">4120 Meridian Court Lakeview, FL 30000</div>

  <h2 class="reviews-title">209 Five-Star Online Reviews</h2>
  <ul class="highlights">
    <li><span class="tick"></span><span>Top-Rated Lakeview<br>Personal Injury Lawyers.</span></li>
    <li><span class="tick"></span><span>Proudly Serving Florida<br>for 40+ Years.</span></li>
    <li><span class="tick"></span><span>We Won over $100,000,000 in<br>Verdicts and Settlements.</span></li>
    <li><span class="tick"></span><span>Call or text for FREE<br>Consultation. Habla Español.</span></li>
  </ul>

  <div class="contact-bar">
    <span class="contact-phone">
      <span class="icon-dot"><svg width="7" height="7" viewBox="0 0 10 10"><path fill="#fff" d="M2,0.5 L3.6,0.5 L4.2,3 L3,3.8 C3.6,5.2 4.8,6.4 6.2,7 L7,5.8 L9.5,6.4 L9.5,8 C9.5,9 8.8,9.5 8,9.5 C4,9.2 0.8,6 0.5,2 C0.5,1.2 1,0.5 2,0.5Z"/></svg></span>
      (555) 014-2287
    </span>
    <span class="contact-web">
      <span class="icon-dot"><svg width="7" height="7" viewBox="0 0 10 10" fill="none" stroke="#fff" stroke-width="0.9"><circle cx="5" cy="5" r="4.2"/><ellipse cx="5" cy="5" rx="1.8" ry="4.2"/><line x1="0.8" y1="5" x2="9.2" y2="5"/></svg></span>
      www.harlowandbenton.com
    </span>
  </div>
</div>
</body>
</html>
```